依頼概要
■依頼の目的/概要
日本酒のラベルデザインをお願いします。
埼玉県加須市の農家(米の生産)・加須市の酒蔵(お酒の醸造)・加須市の酒販店(お酒の販売)が協力して造った加須市の地酒になります。

■依頼詳細
埼玉県加須市の日本酒のラベルデザインの依頼です。
商品名は「純米吟醸 澄川の響」「純米大吟醸 澄川の響」(すみかわのひびき)。
現在のラベルが野暮ったいということと商品規格の変更で、ラベルのリニューアルを検討しております(現在のラベル(純米吟醸と特別純米酒)は添付ファイルをご参照ください)。
純米吟醸は地元埼玉県加須市産の酒米「五百万石」で仕込んだ、スッキリとした口当たり、香りと味のバランスのよいお酒で、純米大吟醸は同じく加須市産の酒米「山田錦」で仕込んだ香りの華やかなフルーティなお酒です。
瓶の形はストレートタイプで、色は緑瓶または緑のフロスト加工瓶を予定しています。
ラベルサイズは縦110mm ×横110mm(若干前後しても大丈夫です)、
「純米吟醸・純米大吟醸」「澄川の響(すみかわの響)」「企画 緑野町の酒米と地酒協議会」の文字を入れて下さい。

全体的にスッキリとした洗練されたデザインが希望です。「純米吟醸」と「純米大吟醸」の2種類になりますが、「同一デザインで色違い」や「デザインの一部を変えて2種類」という感じで統一感を持たせてもらえればと思います。和風・洋風などは問いません。

その他何かご不明な点がございましたら、お気軽にご質問下さい。
よろしくお願いいたします。
■ 選んだ理由

まず協議会の理事会にて投票を行ない得票数の多い7点に絞りました。
その7点の中から、
・キーポイントである酒米が稲穂で表現されているところ
・輪っかが「農家」「酒蔵」「酒販店」の繋がりを連想させる
・スッキリとして洗練されたデザインである
・全体的なバランス
という点を評価し、こちらに決めさせて頂きました。

■ 提案者全員のお礼・コメント

この度は多数のご提案を頂き、誠にありがとうございました。
提案数が多くしかもそれぞれ個性的なため、選定会でも意見が分かれ、選定に時間がかかりましたが、なんとか1点に絞らさせて頂きました。
また機会がありましたらぜひ募集させて頂きたいと思います。
ご応募ありがとうございました。

```html
<!DOCTYPE html>
<html lang="ja">
<head>
<meta charset="utf-8">
<title>澄川の響 ラベル</title>
<link rel="stylesheet" href="https://fonts.googleapis.com/css2?family=Shippori+Mincho:wght@500;700&display=swap">
<style>
  :root {
    --bg: #e9ece4;
    --paper: #ffffff;
    --ink: #141414;
    --gold: #b08a4e;
    --muted: #555555;
    --edge: #d6d8d0;
  }
  html, body {
    margin: 0;
    padding: 0;
    overflow: hidden;
  }
  body {
    width: 880px;
    height: 1200px;
    background: var(--bg);
    position: relative;
    font-family: "Shippori Mincho", serif;
    color: var(--ink);
  }
  .label {
    position: absolute;
    left: 180px;
    width: 520px;
    height: 520px;
    background: var(--paper);
    border: 1px solid var(--edge);
    box-sizing: border-box;
  }
  .label--ginjo { top: 50px; }
  .label--daiginjo { top: 630px; }
  .label__tab {
    position: absolute;
    top: 34px;
    left: 50%;
    transform: translateX(-50%);
    width: 120px;
    height: 26px;
    background: var(--ink);
    color: var(--paper);
    font-size: 13px;
    font-weight: 500;
    letter-spacing: 0.3em;
    line-height: 26px;
    text-align: center;
  }
  .label--daiginjo .label__tab { background: var(--gold); }
  .label__grade {
    position: absolute;
    top: 86px;
    width: 100%;
    text-align: center;
    font-size: 24px;
    font-weight: 700;
    letter-spacing: 0.25em;
    line-height: 1.2;
  }
  .label__name {
    position: absolute;
    top: 150px;
    bottom: 90px;
    left: 0;
    right: 0;
    display: flex;
    align-items: center;
    justify-content: center;
    font-size: 84px;
    font-weight: 700;
    line-height: 1;
    letter-spacing: 0.08em;
    color: var(--ink);
  }
  .label__planner {
    position: absolute;
    bottom: 34px;
    width: 100%;
    text-align: center;
    font-size: 13px;
    font-weight: 500;
    letter-spacing: 0.12em;
    color: var(--muted);
  }
</style>
</head>
<body>

<section class="label label--ginjo">
  <div class="label__tab">埼玉の地酒</div>
  <div class="label__grade">純米吟醸</div>
  <div class="label__name">澄川の響</div>
  <div class="label__planner">企画　緑野町の酒米と地酒協議会</div>
</section>

<section class="label label--daiginjo">
  <div class="label__tab">埼玉の地酒</div>
  <div class="label__grade">純米大吟醸</div>
  <div class="label__name">澄川の響</div>
  <div class="label__planner">企画　緑野町の酒米と地酒協議会</div>
</section>

</body>
</html>
```